Bluestone Advisory & Mgmt - Professional Business Cards

Hi!

I am a Real Estate Developer and Construction Consultant.

I have a lot of inspiration from previous designs and would be open to using the attached Designs as a starting point. I would like to see these styles incorporated into your designs.

I really need professional business card to go with it that includes my important info.

Look forward to seeing your designs!.

Target Market(s)

My Target market are building owners, lawyers, consultants.

Industry/Entity Type

Real Estate Development

Contact Information for Business Card

My Name: Dorian Pelkey
My Title: Principle
Company Name: Bluestone Advisory & Mgmt, LLC
Address: 348 West 71st Street, 9th FL New York, NY 10010
Mobile: 917.806.3971
Website: bam-hvx.example

Font styles to use
Serif
Sans Serif

Colors

Designer to choose colors to be used in the design.

Requirements
Must have
• Must incorporate the logo attached or have new that looks similar.
• Must use professional font that will be seen and judged by wealthy land owners and developers.
• Must incorporate some of the color green.
Should not have
• Photo's or pictures of people or buildings of any kind.

```html
<!DOCTYPE html>
<html lang="en">
<head>
<meta charset="utf-8">
<title>Bluestone Advisory &amp; Mgmt - Professional Business Cards</title>
<link rel="stylesheet" href="https://fonts.googleapis.com/css2?family=Arimo:wght@400;700&family=Libre+Bodoni:wght@400&display=swap">
<style>
  :root {
    --page: #ffffff;
    --ink-cream: #d8cfae;
    --ink-light: #f1ecdc;
    --mark-muted: #6e6548;
    --front-top: #070705;
    --front-mid: #1b1505;
    --front-bottom: #3a2a06;
    --back-grey: #7a7a7a;
    --back-mark: #2f2f2f;
  }
  * { margin: 0; padding: 0; box-sizing: border-box; }
  html, body {
    width: 1200px; height: 1200px; overflow: hidden;
    background: var(--page);
  }
  .sheet { position: relative; width: 1200px; height: 1200px; }
  .card {
    position: absolute; left: 150px; width: 934px; height: 534px;
    overflow: hidden;
  }
  .card-front {
    top: 32px;
    background: linear-gradient(170deg, var(--front-top) 0%, var(--front-mid) 55%, var(--front-bottom) 100%);
    color: var(--ink-cream);
    font-family: "Arimo", Arial, sans-serif;
    text-align: center;
  }
  .card-back { top: 638px; height: 533px; background: var(--back-grey); }

  .company {
    position: absolute; top: 81px; left: 0; right: 0;
    font-size: 43px; line-height: 1; font-weight: 400; letter-spacing: 0.3px;
    text-decoration: underline; text-decoration-thickness: 2px; text-underline-offset: 4px;
  }
  .address {
    position: absolute; top: 133px; left: 0; right: 0;
    font-family: "Libre Bodoni", "Bodoni Moda", serif;
    font-size: 21px; line-height: 1; letter-spacing: 4.2px; color: var(--ink-light);
  }
  .contact {
    position: absolute; top: 164px; left: 0; right: 0;
    display: flex; justify-content: center; gap: 28px;
    font-size: 20px; line-height: 1; color: var(--ink-light);
  }
  .contact-item { display: flex; align-items: center; gap: 5px; }
  .contact-item svg { width: 16px; height: 16px; }
  .name {
    position: absolute; top: 260px; left: 0; right: 0;
    font-size: 78px; line-height: 1; font-weight: 400; letter-spacing: 0.5px;
    text-decoration: underline; text-decoration-thickness: 2px; text-underline-offset: 5px;
  }
  .title {
    position: absolute; top: 340px; left: 0; right: 0;
    line-height: 1;
  }
  .title span {
    display: inline-block; font-size: 19px; line-height: 1;
    border-bottom: 1.5px solid var(--ink-cream); padding: 0 16px 1px;
  }
  .brand-small {
    position: absolute; top: 400px; left: 0; right: 0;
    font-weight: 700; font-size: 52px; line-height: 1;
    color: var(--mark-muted); letter-spacing: -2px;
  }
  .brand-large {
    position: absolute; inset: 0;
    display: flex; align-items: center; justify-content: center;
    font-family: "Arimo", Arial, sans-serif; font-weight: 700;
    font-size: 240px; line-height: 1; letter-spacing: -12px; color: var(--back-mark);
  }
</style>
</head>
<body>
<main class="sheet">
  <section class="card card-front">
    <h1 class="company">Bluestone Advisory &amp; Mgmt, LLC</h1>
    <p class="address">348 West 71st Street, 9th FL New York, NY 10010</p>
    <div class="contact">
      <span class="contact-item">
        <svg viewBox="0 0 16 16" aria-hidden="true"><circle cx="8" cy="8" r="7" fill="none" stroke="#f1ecdc" stroke-width="1.2"/><path d="M5 11 L11 5" stroke="#f1ecdc" stroke-width="1.6" stroke-linecap="round"/><path d="M4.5 10 L6 11.5 M10 4.5 L11.5 6" stroke="#f1ecdc" stroke-width="1.4"/></svg>
        917.806.3971
      </span>
      <span class="contact-item">
        <svg viewBox="0 0 16 16" aria-hidden="true"><g fill="none" stroke="#f1ecdc" stroke-width="1"><circle cx="8" cy="8" r="7"/><ellipse cx="8" cy="8" rx="3" ry="7"/><path d="M1 8 H15 M2 4.5 H14 M2 11.5 H14"/></g></svg>
        bam-hvx.example
      </span>
    </div>
    <h2 class="name">Dorian Pelkey</h2>
    <p class="title"><span>PRINCIPLE</span></p>
    <div class="brand-small">BAM</div>
  </section>
  <section class="card card-back">
    <div class="brand-large">BAM</div>
  </section>
</main>
</body>
</html>
```